Brightpath Holdings Business Card

Create a two sided, high gloss, quality business card for Brightpath Holdings.

Target Market(s)

People wanting to purchase, scale, and sell businesses.

Industry/Entity Type

Entrepreneurs

Contact Information for Business Card

One line: Dana Velko, CPA, CMA Another line: Entrepreneur & Investor Another line: Business Ownership Transition Expert Another line: Multi-State Licensed Real Estate Broker Phone 954-BRTPATH (278-7284) Email Dana@Brightpath Holdings.example Website www.Brightpath.example

Requirements
Must have
• Black Card, logo on one side, all other information on the other side including a small logo.
Nice to have
• Possibly add a tagline "Helping entrepreneurs live a life they don't need a vacation from"
Should not have
• There will not be a mailing address on these cards.

```html
<!DOCTYPE html>
<html lang="en">
<head>
<meta charset="utf-8">
<title>Brightpath Holdings Business Card</title>
<link href="https://fonts.googleapis.com/css2?family=Montserrat:wght@400;500;700&family=Oswald:wght@500&display=swap" rel="stylesheet">
<style>
  :root {
    --stage: #3b3b3d;
    --card: #111112;
    --card-edge: #b8923f;
    --gold: #d1a94f;
    --white: #f2f2f2;
    --silver: #a9a9ab;
  }
  * { box-sizing: border-box; margin: 0; padding: 0; }
  html, body { width: 1200px; height: 1200px; overflow: hidden; }
  body {
    background: var(--stage);
    display: flex; flex-direction: column; align-items: center; justify-content: center;
    gap: 40px;
    font-family: "Montserrat", sans-serif;
  }
  .card {
    position: relative;
    width: 900px; height: 514px;
    background: linear-gradient(160deg, #1a1a1b 0%, var(--card) 60%, #0c0c0d 100%);
    border-radius: 34px;
    border: 2px solid var(--card-edge);
    box-shadow: 0 18px 40px rgba(0,0,0,.45);
    overflow: hidden;
  }
  /* front */
  .front .identity { position: absolute; left: 70px; top: 120px; }
  .front .name {
    color: var(--gold); font-weight: 700; font-size: 44px; letter-spacing: 2px;
    text-transform: uppercase; line-height: 1;
  }
  .front .titles {
    margin-top: 10px; color: var(--white); font-size: 14.5px; font-weight: 500;
    text-transform: uppercase; line-height: 1.25; letter-spacing: .3px;
  }
  .front .contacts { list-style: none; margin-top: 22px; }
  .front .contacts li {
    display: flex; align-items: center; gap: 14px;
    color: var(--white); font-size: 22px; line-height: 1.5;
  }
  .front .contacts svg { width: 22px; height: 22px; flex: none; }
  .front .brand-mark {
    position: absolute; right: 60px; top: 110px;
    display: flex; align-items: center; gap: 12px;
    color: var(--gold);
  }
  .brand-dot { border-radius: 50%; border: 3px solid currentColor; }
  .front .brand-dot { width: 36px; height: 36px; }
  .front .brand-name { font-weight: 700; font-size: 30px; white-space: nowrap; }
  .front .tagline {
    position: absolute; left: 70px; right: 60px; bottom: 50px;
    font-family: "Oswald", sans-serif; font-weight: 500; font-size: 22px;
    color: var(--gold); text-transform: uppercase; letter-spacing: .6px;
    white-space: nowrap;
  }
  /* back */
  .back { display: flex; align-items: center; justify-content: center; }
  .back .brand-mark { display: flex; align-items: center; gap: 24px; color: var(--silver); }
  .back .brand-dot { width: 78px; height: 78px; border-width: 5px; }
  .back .brand-name { font-weight: 700; font-size: 66px; white-space: nowrap; }
</style>
</head>
<body>
  <section class="card front" aria-label="Card front">
    <div class="identity">
      <h1 class="name">Dana Velko</h1>
      <p class="titles">CPA, CMA, Entrepreneur, Investor<br>Business Ownership Transition Expert<br>Multi-State Licensed Real Estate Broker</p>
      <ul class="contacts">
        <li>
          <svg viewBox="0 0 24 24" aria-hidden="true"><path fill="#d1a94f" d="M6.6 10.8a15.1 15.1 0 0 0 6.6 6.6l2.2-2.2c.3-.3.7-.4 1-.2 1.1.4 2.3.6 3.6.6.6 0 1 .4 1 1V20c0 .6-.4 1-1 1A17 17 0 0 1 3 4c0-.6.4-1 1-1h3.5c.6 0 1 .4 1 1 0 1.3.2 2.5.6 3.6.1.3 0 .7-.2 1z"/></svg>
          954-BRTPATH (278-7284)
        </li>
        <li>
          <svg viewBox="0 0 24 24" aria-hidden="true" fill="none" stroke="#d1a94f" stroke-width="1.8"><circle cx="12" cy="12" r="9.5"/><ellipse cx="12" cy="12" rx="4" ry="9.5"/><path d="M2.5 12h19M4 7h16M4 17h16"/></svg>
          www.Brightpath.example
        </li>
        <li>
          <svg viewBox="0 0 24 24" aria-hidden="true" fill="none" stroke="#d1a94f" stroke-width="1.8"><rect x="2.5" y="5" width="19" height="14" rx="1"/><path d="M2.5 5l9.5 8 9.5-8"/></svg>
          Dana@BrightpathHoldings.example
        </li>
      </ul>
    </div>
    <div class="brand-mark">
      <span class="brand-dot" aria-hidden="true"></span>
      <span class="brand-name">Brightpath Holdings</span>
    </div>
    <p class="tagline">Helping entrepreneurs live a life they don't need a vacation from</p>
  </section>

  <section class="card back" aria-label="Card back">
    <div class="brand-mark">
      <span class="brand-dot" aria-hidden="true"></span>
      <span class="brand-name">Brightpath Holdings</span>
    </div>
  </section>
</body>
</html>
```